Magazine Ad for Admissions Consulting Company

1. The ad should be a half-page ad. Ad specifications: 7.25 x 4.75" (please also see the attached AdSpecSheet for information on trim size.)

2. I attach a rough draft of the ad. The ad that you create should have all of the information contained in this rough draft. (it should have the Average Acceptance Rates table, the advertisement of the webinar, the logo, our motto, and our contact information).

3. Currently the ad looks unprofessional and not stylish. Feel free to change the colors, the fonts, the picture in the background, the size of the various components, and anything else you seem fit.

our website: www.brackenvaleprep.com

Target Market(s)

Affluent college alumni, who are parents of high-school aged children.

Industry/Entity Type

It Company

Colors
0455a3
3276b5
0292cd
33a6d7
85cae6
85abd2
ffffff
eff8fb
eaf1f7

Requirements
Must have
• Everything in the ad must be vector-based.
Nice to have
• We want the ad to look stylish, professional and upmarket.

```html
<!DOCTYPE html>
<html lang="en">
<head>
<meta charset="utf-8">
<title>Brackenvale Prep Consulting – Half-page Ad</title>
<link rel="stylesheet" href="https://fonts.googleapis.com/css2?family=Open+Sans:ital,wght@0,400;0,600;0,700;1,400;1,600&display=swap">
<style>
  :root {
    --navy: #0455a3;
    --blue: #3276b5;
    --bar: #2a79b0;
    --sky: #0292cd;
    --sky-soft: #85cae6;
    --mist: #eff8fb;
    --pale: #eaf1f7;
    --ink: #1d2a38;
    --grey-head: #c9ccd0;
    --grey-row: #e4e6e8;
    --white: #ffffff;
    --stage: #e9ecef;
  }
  * { box-sizing: border-box; margin: 0; padding: 0; }
  html, body { width: 1200px; height: 784px; overflow: hidden; }
  body {
    background: var(--stage);
    font-family: "Open Sans", Arial, sans-serif;
    color: var(--ink);
    position: relative;
  }
  .ad {
    position: absolute; left: 50px; top: 32px;
    width: 1100px; height: 720px;
    background: linear-gradient(180deg, var(--white) 0%, var(--mist) 55%, var(--pale) 100%);
    overflow: hidden;
    box-shadow: 0 4px 18px rgba(0,0,0,.12);
  }
  .brand {
    position: absolute; left: 360px; top: 34px; width: 520px;
    text-align: center;
  }
  .brand-name {
    display: inline-flex; align-items: center; gap: 12px;
    font-size: 30px; font-weight: 600; color: var(--navy);
  }
  .brand-dot { width: 22px; height: 22px; border-radius: 50%; background: var(--sky); }
  .motto { margin-top: 14px; font-size: 17px; font-weight: 700; color: var(--ink); }
  .motto-sub { font-size: 16px; font-style: italic; color: var(--sky); }

  .rates { position: absolute; left: 30px; top: 168px; width: 520px; }
  .rates-title {
    background: var(--navy); color: var(--white);
    font-size: 15px; font-weight: 700; font-style: italic;
    padding: 7px 10px; text-transform: uppercase;
  }
  .rates table { width: 100%; border-collapse: collapse; font-size: 13.5px; }
  .rates th {
    background: var(--grey-head); font-weight: 400; font-size: 13px;
    text-align: left; padding: 6px 8px; line-height: 1.25; vertical-align: bottom;
    border-left: 2px solid var(--white);
  }
  .rates th:first-child { background: transparent; border-left: none; }
  .rates td { padding: 6px 8px; border-left: 2px solid var(--white); border-top: 2px solid var(--white); }
  .rates td:first-child { border-left: none; }
  .rates tr:nth-child(odd) td:not(:first-child) { background: var(--grey-row); }
  .rates .col-school { width: 46%; }

  .webinar { position: absolute; left: 600px; top: 208px; width: 470px; }
  .webinar-title { font-size: 25px; font-weight: 700; color: var(--navy); text-transform: uppercase; letter-spacing: .5px; }
  .webinar-topic { font-size: 17px; font-style: italic; margin-top: 4px; line-height: 1.3; }
  .webinar-live { font-size: 19px; font-weight: 700; margin-top: 16px; }
  .webinar-when { font-size: 16px; font-weight: 600; line-height: 1.35; }

  .photo {
    position: absolute; left: 470px; top: 410px; width: 630px; height: 230px;
    background: linear-gradient(90deg, rgba(133,171,210,0) 0%, rgba(133,171,210,.55) 25%, #85abd2 60%, #3276b5 100%);
  }

  .register {
    position: absolute; left: 0; bottom: 0; width: 100%; height: 80px;
    background: var(--bar); color: var(--white);
    display: flex; align-items: center; gap: 22px; padding: 0 34px;
    font-size: 17px; font-weight: 700;
  }
  .register-label { font-style: italic; margin-right: 40px; }
  .register-phone { display: inline-flex; align-items: center; gap: 8px; }
  .register-sep { font-weight: 400; }
</style>
</head>
<body>
  <article class="ad">
    <header class="brand">
      <div class="brand-name"><span class="brand-dot"></span>Brackenvale Prep Consulting</div>
      <p class="motto">One-on-One College Admissions Counseling</p>
      <p class="motto-sub">From Former Admissions Officers</p>
    </header>

    <section class="rates">
      <div class="rates-title">2015 Average Acceptance Rates</div>
      <table>
        <thead>
          <tr><th class="col-school"></th><th>National<br>Acceptance Rate</th><th>Brackenvale<br>Admissions<br>Acceptance Rate</th></tr>
        </thead>
        <tbody>
          <tr><td>Halvorsen University</td><td>6.1%</td><td>29.7%</td></tr>
          <tr><td>Ridgemont University</td><td>14.9%</td><td>45.2%</td></tr>
          <tr><td>Ashcombe University</td><td>5.3%</td><td>15.4%</td></tr>
          <tr><td>NIT</td><td>8%</td><td>27.3%</td></tr>
          <tr><td>WBU</td><td>35.5%</td><td>63.9%</td></tr>
          <tr><td>Fairhaven University</td><td>7%</td><td>21.4%</td></tr>
          <tr><td>Linwood University</td><td>5.1%</td><td>27.3%</td></tr>
          <tr><td>UC Marlow</td><td>16%</td><td>44.2%</td></tr>
          <tr><td>University of Easton</td><td>8.8%</td><td>32.4%</td></tr>
          <tr><td>University of Carrow</td><td>9.9%</td><td>30.4%</td></tr>
        </tbody>
      </table>
    </section>

    <div class="photo" role="img" aria-label="Blue-toned photo of students and a counselor working together around a table"></div>

    <section class="webinar">
      <h2 class="webinar-title">Complimentary Webinar</h2>
      <p class="webinar-topic">“How To Be Accepted by Linwood and<br>Elmstead League Universities”</p>
      <p class="webinar-live">Live Answers to Live Questions</p>
      <p class="webinar-when">3-4 pm PST (6-7 pm EST)<br>Sunday, September 18, 2016</p>
    </section>

    <footer class="register">
      <span class="register-label">To register for the complimentary seminar:</span>
      <span class="register-phone">
        <svg width="20" height="20" viewBox="0 0 20 20" aria-hidden="true">
          <circle cx="10" cy="10" r="10" fill="#ffffff"/>
          <path d="M6.5 5.2c.4-.4 1-.4 1.3 0l1.2 1.6c.3.4.3.9-.1 1.2l-.7.6c.6 1.2 1.6 2.2 2.8 2.8l.6-.7c.3-.4.8-.4 1.2-.1l1.6 1.2c.4.3.4.9 0 1.3l-.8.8c-.6.6-1.6.7-2.4.3-2.2-1.1-4-2.900-5.1-5.1-.4-.8-.3-1.8.3-2.4z" fill="#2a79b0"/>
        </svg>
        1.646.555.0142
      </span>
      <span class="register-sep">|</span>
      <span class="register-web">www.brackenvaleprep.com/webinar</span>
    </footer>
  </article>
</body>
</html>
```